Logo for Japanese Restaurant
Sushi Mareta
Project: Logo for Japanese Restaurant
Logo for Japanese Restaurant - Food
Creative Brief
Simple
2843 Linwell Avenue New York, NY 10241
sushimaretanyc@pondmail.example
My vision is to have a business card where on the back side is our logo and front side is our restaurant information with our logo be in the background.

```html
<!DOCTYPE html>
<html lang="en">
<head>
<meta charset="utf-8">
<title>Mareta House — Business Card</title>
<link href="https://fonts.googleapis.com/css2?family=Open+Sans:wght@400;600&family=Oswald:wght@600&display=swap" rel="stylesheet">
<style>
  :root {
    --stage: #1b1b1b;
    --card-dark: #0c0c0c;
    --card-light: #ffffff;
    --red: #d8222a;
    --orange: #f08a1c;
    --ink: #3a3a3a;
    --muted: #8a8a8a;
    --rule: #cfcfcf;
  }
  * { margin: 0; padding: 0; box-sizing: border-box; }
  html, body { width: 1200px; height: 1023px; overflow: hidden; }
  body {
    background: var(--stage);
    font-family: "Open Sans", Arial, sans-serif;
    display: flex;
    flex-direction: column;
    align-items: center;
    justify-content: center;
    gap: 60px;
  }
  .card {
    width: 760px;
    height: 434px;
    position: relative;
    box-shadow: 0 14px 40px rgba(0,0,0,.55);
  }
  .card::after {
    content: "";
    position: absolute;
    left: 0; right: 0; bottom: 0;
    height: 6px;
    background: var(--red);
  }
  .card--back { background: var(--card-dark); }
  .card--front { background: var(--card-light); }

  .brand {
    display: flex;
    flex-direction: column;
    align-items: center;
    gap: 14px;
  }
  .brand__dot {
    width: 74px; height: 74px;
    border-radius: 50%;
    background: var(--red);
  }
  .brand__name {
    font-family: "Oswald", Impact, sans-serif;
    font-weight: 600;
    font-size: 40px;
    letter-spacing: 1px;
    text-transform: uppercase;
    line-height: 1;
  }
  .card--back .brand {
    position: absolute;
    left: 50%; top: 50%;
    transform: translate(-50%, -50%);
  }
  .card--back .brand__name { color: #ffffff; }

  .card--front .brand {
    position: absolute;
    left: 100px; top: 200px;
  }
  .card--front .brand__name { color: var(--ink); font-size: 34px; }
  .card--front .brand__dot { width: 64px; height: 64px; }

  .contact {
    position: absolute;
    left: 400px; top: 70px;
    padding-left: 14px;
    border-left: 1px solid var(--rule);
    color: var(--muted);
    font-size: 13px;
    line-height: 1.55;
  }
  .contact__name {
    color: var(--red);
    font-weight: 600;
    font-size: 24px;
    line-height: 1.2;
  }
  .contact__role { margin-bottom: 26px; }
  .contact__address { margin-bottom: 22px; }
  .contact__line {
    display: flex;
    align-items: center;
    gap: 8px;
  }
  .contact__line svg { width: 11px; height: 11px; flex: none; }
</style>
</head>
<body>
  <section class="card card--back">
    <div class="brand">
      <span class="brand__dot"></span>
      <span class="brand__name">Mareta House</span>
    </div>
  </section>

  <section class="card card--front">
    <div class="brand">
      <span class="brand__dot"></span>
      <span class="brand__name">Mareta House</span>
    </div>

    <div class="contact">
      <p class="contact__name">Sushi Mareta</p>
      <p class="contact__role">Owner</p>
      <p class="contact__address">2843 Linwell Avenue<br>New York, NY 10241</p>
      <p class="contact__line">
        <svg viewBox="0 0 12 12" aria-hidden="true"><path d="M3 1h2l1 3-1.5 1a6 6 0 0 0 2.5 2.5L8 6l3 1v2a2 2 0 0 1-2 2A9 9 0 0 1 1 3a2 2 0 0 1 2-2z" fill="var(--orange)"/></svg>
        347 555 0148
      </p>
      <p class="contact__line">
        <svg viewBox="0 0 12 12" aria-hidden="true"><rect x="3" y="0.5" width="6" height="11" rx="1.2" fill="none" stroke="var(--orange)" stroke-width="1.3"/><circle cx="6" cy="9.5" r=".8" fill="var(--orange)"/></svg>
        347 555 0172
      </p>
      <p class="contact__line">
        <svg viewBox="0 0 12 12" aria-hidden="true"><rect x="0.5" y="2" width="11" height="8" fill="var(--orange)"/><path d="M0.5 2l5.5 4.5L11.5 2" fill="none" stroke="#fff" stroke-width="1"/></svg>
        sushimaretanyc@pondmail.example
      </p>
    </div>
  </section>
</body>
</html>
```